Anzeigengestaltung für Vertrieb von Kunststoffgittern
Zielgruppe
Vertrieb von Kunststoffgittern aus eigener Herstellung zur Bodenbefestigung. Einsatz in der Pferdehaltung. Böden von Paddocks und Ausläufen, Reitplätze, Reithallen, Führanlagen, Roundpen. Parkplatzbefestigung, Weidewege Freß- und Tränkplätze, Offenställe.
Wir benötigen eine neue Anzeige in diversen Pferdezeitschriften. Sie sollte ansprechend, mit hohem Wiedererkennunswert sein
Aufgabenstellung
Anzeige sollte für die Größe: 1/4 Seite mit Satzspiegel 43 x 270 mm, längs und 184 x 67 mm quer passen.
Die Anzeige sollte klar und ansprechend strukturiert sein, sie soll der Imagepflege dienen.
Die Farben Grün / Gelb wie im logo sollten vorherrschen. Ein innovativer Text ist gewünscht.
Zur Information kann die website: www.talbrek-gz.com dienen.
Weitere Fotos können zur Verfügung gestellt werden.

```html
<!DOCTYPE html>
<html lang="de">
<head>
<meta charset="utf-8">
<title>Talbrek GZ – Anzeige</title>
<link href="https://fonts.googleapis.com/css2?family=Roboto+Condensed:wght@400;700&display=swap" rel="stylesheet">
<style>
  :root {
    --forest: #11251a;
    --amber: #e39636;
    --white: #ffffff;
    --page: #ffffff;
    --photo-top: #8a8560;
    --photo-bottom: #c9a466;
    --inset: #343a35;
  }
  * { margin: 0; padding: 0; box-sizing: border-box; }
  html, body {
    width: 848px; height: 1200px; overflow: hidden;
    background: var(--page);
    font-family: "Roboto Condensed", "Arial Narrow", sans-serif;
  }
  .ad {
    position: absolute; left: 301px; top: 51px;
    width: 175px; height: 1091px;
    display: flex; flex-direction: column;
  }
  .intro {
    height: 332px; background: var(--forest); color: var(--white);
    padding: 27px 8px 0 14px;
  }
  .headline {
    font-weight: 700; font-size: 43px; line-height: 42px; letter-spacing: -0.3px;
  }
  .lead {
    margin-top: 12px; font-size: 17px; line-height: 21.3px; font-weight: 400;
  }
  .accent-band { height: 17px; background: var(--amber); }
  .photo {
    position: relative; height: 440px;
    background: linear-gradient(180deg, var(--photo-top) 0%, var(--photo-bottom) 100%);
  }
  .product-inset {
    position: absolute; left: 49px; top: 318px;
    width: 112px; height: 112px; border-radius: 50%;
    border: 3px solid var(--forest);
    background: var(--inset);
  }
  .divider-band { height: 16px; background: var(--forest); }
  .brand {
    height: 60px; background: var(--white);
    display: flex; align-items: center; justify-content: center; gap: 8px;
  }
  .brand-mark { width: 14px; height: 14px; background: var(--amber); }
  .brand-name { font-size: 27px; font-weight: 400; color: var(--forest); letter-spacing: 0.5px; }
  .contact {
    flex: 1; background: var(--amber); color: var(--forest);
    padding: 21px 8px 0 13px; font-size: 17.5px; line-height: 21.5px;
    font-style: normal;
  }
  .contact p + p { margin-top: 6px; }
  .contact strong { font-weight: 700; }
</style>
</head>
<body>
  <div class="ad">
    <section class="intro">
      <h1 class="headline">Erfolg<br>braucht<br>System!</h1>
      <p class="lead">Wir bieten Ihnen in<br>der Pferdehaltung<br>und dem -sport eine<br>Vielzahl von System-<br>komponenten für den<br>Bodenbereich.</p>
    </section>
    <div class="accent-band"></div>
    <div class="photo" role="img" aria-label="Foto: zwei braune Pferde spielen auf einem Sandauslauf">
      <div class="product-inset" role="img" aria-label="Foto: schwarzes Kunststoff-Bodengitter in Nahaufnahme"></div>
    </div>
    <div class="divider-band"></div>
    <div class="brand">
      <span class="brand-mark"></span>
      <span class="brand-name">talbrek GZ</span>
    </div>
    <address class="contact">
      <p><strong>Talbrek GZ</strong><br>Lindenweg 12<br>08115 Morhausen</p>
      <p>T: 034 21 – 58 17 40<br>F: 034 21 – 58 17 41</p>
      <p>info@talbrek-gz.com<br><strong>www.talbrek-gz.com</strong></p>
    </address>
  </div>
</body>
</html>
```